Christmas Collection Candle Label Design

Looking to update our existing Christmas Candle Collection labels. Labels should reflect the overall feel of our brand- www.wickmerelane.ca
Want to include some color elements. Holiday colors added into design but more muted/ earthy tones not vibrant colors . Metallic elements and line art botanical illustration. Fonts should be more align to brand
Scents
Holiday Tree
Candy Cane
Sugar and Spice
Joyeaux Noel

```html
<!DOCTYPE html>
<html lang="en">
<head>
<meta charset="utf-8">
<title>Joyeaux Noel – Christmas Collection Candle Label</title>
<link rel="stylesheet" href="https://fonts.googleapis.com/css2?family=Source+Serif+4:opsz,wght@8..60,700&family=Barlow:wght@500&display=swap">
<style>
  :root {
    --paper: #ffffff;
    --botanical-cream: #f4f7ef;
    --botanical-soft: #cde7da;
    --botanical-line: #a6d4be;
    --label-mint: #93c7b1;
    --ink: #121212;
    --rule: #3a4a43;
  }
  html, body {
    margin: 0;
    padding: 0;
    width: 1200px;
    height: 800px;
    overflow: hidden;
    background: var(--paper);
  }
  .label {
    position: relative;
    width: 1200px;
    height: 800px;
    overflow: hidden;
  }
  .botanical-backdrop {
    position: absolute;
    inset: 0;
    background:
      radial-gradient(ellipse 320px 260px at 8% 12%, var(--botanical-line) 0%, transparent 100%),
      radial-gradient(ellipse 300px 240px at 52% 4%, var(--botanical-line) 0%, transparent 100%),
      radial-gradient(ellipse 320px 280px at 94% 14%, var(--botanical-line) 0%, transparent 100%),
      radial-gradient(ellipse 260px 300px at 4% 55%, var(--botanical-soft) 0%, transparent 100%),
      radial-gradient(ellipse 260px 300px at 97% 52%, var(--botanical-soft) 0%, transparent 100%),
      radial-gradient(ellipse 340px 260px at 14% 96%, var(--botanical-line) 0%, transparent 100%),
      radial-gradient(ellipse 320px 240px at 50% 98%, var(--botanical-soft) 0%, transparent 100%),
      radial-gradient(ellipse 340px 280px at 90% 94%, var(--botanical-line) 0%, transparent 100%),
      var(--botanical-cream);
  }
  .name-panel {
    position: absolute;
    left: 190px;
    top: 146px;
    width: 820px;
    height: 507px;
    background: var(--label-mint);
  }
  .scent-title {
    position: absolute;
    left: 85px;
    top: 116px;
    margin: 0;
    font-family: "Source Serif 4", Georgia, serif;
    font-weight: 700;
    font-size: 74px;
    line-height: 80px;
    letter-spacing: 0.1em;
    color: var(--ink);
  }
  .collection-arc {
    position: absolute;
    left: 0;
    top: 0;
    width: 820px;
    height: 507px;
    overflow: visible;
  }
  .collection-arc text {
    font-family: "Barlow", Arial, sans-serif;
    font-weight: 500;
    font-size: 10.5px;
    letter-spacing: 0.08em;
    fill: var(--ink);
  }
  .details {
    position: absolute;
    left: 85px;
    width: 650px;
    top: 400px;
    font-family: "Barlow", Arial, sans-serif;
    font-weight: 500;
    font-size: 14.5px;
    letter-spacing: 0.04em;
    color: var(--ink);
  }
  .details-row {
    display: flex;
    justify-content: space-between;
    line-height: 20px;
  }
  .details-rule {
    height: 1px;
    background: var(--rule);
    margin: 7px 0 9px;
  }
  .size-burn {
    display: flex;
  }
  .size { margin-right: 66px; }
  .divider { margin-right: 25px; }
</style>
</head>
<body>
  <main class="label">
    <div class="botanical-backdrop" role="img" aria-label="Line art botanical illustration of large flowers and leaves in soft mint lines on cream, framing the label on all sides"></div>

    <section class="name-panel">
      <h1 class="scent-title">JOYEAUX<br>NOEL</h1>

      <svg class="collection-arc" viewBox="0 0 820 507" aria-label="Christmas Collection">
        <path id="collection-curve" d="M 258 300 A 72 72 0 0 0 360 226" fill="none"/>
        <text><textPath href="#collection-curve">CHRISTMAS COLLECTION</textPath></text>
      </svg>

      <div class="details">
        <div class="details-row">
          <span class="brand-name">WICKMERE LANE</span>
          <span class="ingredients">MADE WITH PLANT BASED BOTANICAL</span>
        </div>
        <div class="details-rule"></div>
        <div class="details-row">
          <span class="origin">MADE IN CANADA</span>
          <span class="size-burn"><span class="size">13 OZ</span><span class="divider">|</span><span class="burn-time">120 MIN BURN TIME</span></span>
        </div>
      </div>
    </section>
  </main>
</body>
</html>
```